Manufacturing company needs new business card.

I need a unique Business Card that will truly stand out. Nothing too busy. Simple is good, right? Not looking for a standard design either. No cookie cutter layout. I am just looking for something interesting and a bit different. Does't have to completely off the wall crazy, just not your run of the mill business card. Clean and modern with a touch of industrial.

Target Market(s)

Air conditioning industry, Architects, builders.

Industry/Entity Type

Business

Contact Information for Business Card

Details to be included on card are:

Peter Vance
Managing Director

T: 1300 847 519
M: 0428 593 174
W: www.brenvaleworks.com.au
E: peter.vance@brenvaleworks.com.au
A: 58 Harwick Lane, Sydney NSW 2000

Font styles to use
Sans Serif

Colors
0355a3
848484
fbfbfb

Requirements
Must have
• Card design must be landscape.

```html
<!DOCTYPE html>
<html lang="en">
<head>
<meta charset="utf-8">
<title>Brenvale Works – Business Card</title>
<link rel="stylesheet" href="https://fonts.googleapis.com/css2?family=Open+Sans:wght@400;600;700&display=swap">
<style>
  :root {
    --brand-blue: #0355a3;
    --brand-blue-light: #2f6cc9;
    --brand-grey: #848484;
    --paper: #fbfbfb;
    --paper-shade: #b9b9b9;
    --ink: #1a1a1a;
    --backdrop: #d6d4d4;
  }
  * { margin: 0; padding: 0; box-sizing: border-box; }
  html, body {
    width: 1200px; height: 800px; overflow: hidden;
    background: var(--backdrop);
    font-family: "Open Sans", sans-serif;
  }
  .stage {
    width: 1200px; height: 800px;
    display: flex; align-items: center; justify-content: center; gap: 40px;
  }
  .card {
    position: relative;
    width: 540px; height: 310px;
    border-radius: 16px;
    overflow: hidden;
    box-shadow: 0 6px 18px rgba(0,0,0,.18);
  }

  /* Front */
  .card-front {
    background: linear-gradient(115deg, #ffffff 0%, var(--paper) 35%, #dcdcdc 70%, var(--paper-shade) 100%);
  }
  .person { position: absolute; left: 36px; top: 38px; }
  .person-name { font-size: 29px; color: var(--ink); font-weight: 400; line-height: 1.1; }
  .person-name strong { font-weight: 700; }
  .person-role { font-size: 14px; color: var(--brand-blue); margin-top: 2px; }
  .accent-band {
    position: absolute; left: 0; top: 118px;
    width: 262px; height: 20px; background: var(--brand-blue);
  }
  .accent-tab {
    position: absolute; right: 0; top: 96px;
    width: 30px; height: 18px; background: var(--brand-blue);
  }
  .company {
    position: absolute; left: 276px; top: 112px;
    display: flex; align-items: center; gap: 10px;
  }
  .company-square { width: 22px; height: 22px; background: var(--brand-blue); }
  .company-name { font-size: 21px; font-weight: 600; color: var(--brand-blue); letter-spacing: .2px; }

  .contacts {
    position: absolute; left: 44px; top: 164px;
    list-style: none; font-size: 14px; color: var(--ink);
  }
  .contacts li { display: flex; align-items: center; gap: 12px; height: 25px; }
  .contacts svg { width: 15px; height: 15px; fill: var(--brand-blue); flex: none; }

  /* Back */
  .card-back {
    background: linear-gradient(135deg, var(--brand-blue-light) 0%, var(--brand-blue) 55%, #0a3f86 100%);
  }
  .back-brand {
    position: absolute; right: 36px; bottom: 44px;
    display: flex; align-items: center; gap: 12px;
  }
  .back-brand .company-square { background: #ffffff; width: 26px; height: 26px; }
  .back-brand .company-name { color: #ffffff; font-size: 25px; }
</style>
</head>
<body>
<main class="stage">
  <section class="card card-front" aria-label="Business card front">
    <div class="person">
      <h1 class="person-name">Peter <strong>Vance</strong></h1>
      <p class="person-role">Managing Director</p>
    </div>
    <div class="accent-band"></div>
    <div class="accent-tab"></div>
    <div class="company">
      <span class="company-square"></span>
      <span class="company-name">Brenvale Works</span>
    </div>
    <ul class="contacts">
      <li>
        <svg viewBox="0 0 16 16" aria-hidden="true"><path d="M1 6c0-2 3-3 7-3s7 1 7 3v1h-3V5.5C11 5 10 5 8 5s-3 0-4 .5V7H1zM4 8h8l2 5H2z"/></svg>
        1300 847 519
      </li>
      <li>
        <svg viewBox="0 0 16 16" aria-hidden="true"><path d="M4 1h8v14H4zM5.5 2.5v9h5v-9zM7 12.5h2v1H7z" fill-rule="evenodd"/></svg>
        0428 593 174
      </li>
      <li>
        <svg viewBox="0 0 16 16" aria-hidden="true"><path d="M8 1a7 7 0 1 0 0 14A7 7 0 0 0 8 1zm0 1.2c.9.9 1.6 2.4 1.8 4.2H6.2C6.4 4.6 7.1 3.1 8 2.2zM2.3 7.4h2.8c.1-1.8.6-3.3 1.3-4.3A5.8 5.8 0 0 0 2.3 7.4zm8.6 0h2.8a5.8 5.8 0 0 0-4.1-4.3c.7 1 1.2 2.5 1.3 4.3zM6.2 8.6h3.6C9.6 10.4 8.9 11.9 8 12.8c-.9-.9-1.6-2.4-1.8-4.2zm-3.9 0a5.8 5.8 0 0 0 4.1 4.3c-.7-1-1.2-2.5-1.3-4.3zm8.6 0c-.1 1.8-.6 3.3-1.3 4.3a5.8 5.8 0 0 0 4.1-4.3z"/></svg>
        www.brenvaleworks.com.au
      </li>
      <li>
        <svg viewBox="0 0 16 16" aria-hidden="true"><path d="M1 3h14v10H1zm1.5 1.2L8 8.5l5.5-4.3z"/></svg>
        peter.vance@brenvaleworks.com.au
      </li>
      <li>
        <svg viewBox="0 0 16 16" aria-hidden="true"><path d="M8 1a5 5 0 0 0-5 5c0 4 5 9 5 9s5-5 5-9a5 5 0 0 0-5-5zm0 3a2 2 0 1 1 0 4 2 2 0 0 1 0-4z"/></svg>
        58 Harwick Lane, Sydney NSW 2000
      </li>
    </ul>
  </section>

  <section class="card card-back" aria-label="Business card back">
    <div class="back-brand">
      <span class="company-square"></span>
      <span class="company-name">Brenvale Works</span>
    </div>
  </section>
</main>
</body>
</html>
```